Special offers flyer for IT firm

We need a flyer design for our IT technical services firm based in Melbourne, Australia. We want to advertise two offerings on a double sided flyer.
-
First Offering:
Free computer system health report and audit
- health check of servers, workstations and network
- comprehensive non-technical report including recommendations
-
Second Offering:
Discounted technical support - $80* per hour
- day to day helpdesk support
- system upgrades and migrations
- cloud services design, implementation and support
- web hosting, domain names and email filtering

*exclusive of GST (must denote somewhere in small print)
-
The contact details for the offer must include room for Phone, Email and Web Address.

I am not set on the text, or any particular format, additional images would be good to break up the pages.

Target Market(s)

Professional Services small business owners (under 30 staff)

Industry/Entity Type

Computer

Requirements
Must have
• DL Sized document (210mmx99mm) portrait or landscape, double sided.

```html
<!DOCTYPE html>
<html lang="en">
<head>
<meta charset="utf-8">
<title>TenPeak IT – Special Offers Flyer</title>
<link rel="stylesheet" href="https://fonts.googleapis.com/css2?family=Belleza&family=Lobster&display=swap">
<style>
  :root {
    --stage: #0b0b0b;
    --paper: #ffffff;
    --navy: #1c2440;
    --blue-deep: #12357e;
    --blue-mid: #2a5ca8;
    --blue-bright: #1c6fd0;
    --gold: #f6b41e;
    --gold-shadow: #2e1f08;
    --red-swoosh: #a8301c;
    --bullet-gold: #e9a321;
    --bullet-sky: #6fb6ff;
    --label-grey: #5a5a5a;
    --rule-grey: #4a4a4a;
  }
  * { margin: 0; padding: 0; box-sizing: border-box; }
  html, body { width: 1200px; height: 1183px; overflow: hidden; }
  body { background: var(--stage); position: relative; font-family: "Belleza", sans-serif; }

  .flyer-side { position: absolute; top: 104px; width: 460px; height: 976px; overflow: hidden; }
  .flyer-side--front { left: 117px; }
  .flyer-side--back { left: 624px; }
  .side-art { position: absolute; inset: 0; width: 460px; height: 976px; }

  .brand-name {
    position: absolute; top: 70px; left: 0; width: 460px; text-align: center;
    font-size: 54px; line-height: 60px; color: var(--navy); letter-spacing: 1px;
  }
  .offer-title {
    position: absolute; width: 460px; left: 0; text-align: center;
    font-family: "Lobster", cursive; color: var(--gold);
    font-size: 80px; line-height: 72px;
    text-shadow: 3px 3px 0 var(--gold-shadow), 4px 4px 2px rgba(0,0,0,.4);
  }
  .offer-title--first { top: 222px; }
  .offer-title--second { top: 282px; left: -22px; transform: rotate(-15deg); }

  .offer-subtitle {
    position: absolute; top: 390px; left: 0; width: 460px; text-align: center;
    color: var(--paper); font-size: 36px; line-height: 45px;
  }

  .feature-list { position: absolute; list-style: none; color: var(--paper); }
  .feature-list li { position: relative; }
  .feature-list li::before { content: "\2756"; position: absolute; }
  .feature-list--front { top: 675px; left: 116px; width: 340px; font-size: 25px; line-height: 31.5px; text-transform: uppercase; }
  .feature-list--front li { margin-bottom: 6px; }
  .feature-list--front li::before { left: -29px; color: var(--bullet-gold); font-size: 20px; }
  .feature-list--back { top: 620px; left: 63px; width: 390px; font-size: 25px; line-height: 32px; }
  .feature-list--back li::before { left: -22px; color: var(--bullet-sky); font-size: 18px; }

  .contact-box {
    position: absolute; left: 34px; top: 818px; width: 392px; height: 136px;
    background: var(--paper); border: 1px solid #c9d3e2;
  }
  .contact-row {
    position: absolute; left: 14px; width: 363px; height: 42px;
    font-size: 20px; color: var(--label-grey); line-height: 42px;
  }
  .contact-row:nth-child(1) { top: 6px; border-bottom: 1.5px solid var(--rule-grey); }
  .contact-row:nth-child(2) { top: 48px; border-bottom: 1.5px solid var(--rule-grey); }
  .contact-row:nth-child(3) { top: 90px; }
  .contact-row .colon { position: absolute; left: 124px; }
</style>
</head>
<body>

<section class="flyer-side flyer-side--front">
  <svg class="side-art" viewBox="0 0 428 908" preserveAspectRatio="none">
    <defs>
      <linearGradient id="frontBlue" x1="0" y1="0" x2="1" y2="1">
        <stop offset="0" stop-color="#2a5ca8"/>
        <stop offset="1" stop-color="#163f8a"/>
      </linearGradient>
      <linearGradient id="redSwoosh" x1="0" y1="0" x2="1" y2="0">
        <stop offset="0" stop-color="#8e2414"/>
        <stop offset="1" stop-color="#c7421e"/>
      </linearGradient>
      <linearGradient id="officePhoto" x1="0" y1="0" x2="0" y2="1">
        <stop offset="0" stop-color="#2a5ca8" stop-opacity="0"/>
        <stop offset=".35" stop-color="#6d7f99"/>
        <stop offset=".7" stop-color="#9b7a55"/>
        <stop offset="1" stop-color="#7a5232"/>
      </linearGradient>
    </defs>
    <rect width="428" height="908" fill="#ffffff"/>
    <path d="M0 206 Q190 160 428 158 L428 176 Q200 178 0 222 Z" fill="#f2b11c"/>
    <path d="M0 220 Q200 176 428 172 L428 908 L0 908 Z" fill="url(#frontBlue)"/>
    <path d="M0 490 Q220 470 428 448 Q240 492 0 524 Z" fill="url(#redSwoosh)"/>
    <rect y="600" width="428" height="308" fill="url(#officePhoto)" role="img" aria-label="Photo of an office worker at a desk with computers"/>
  </svg>

  <div class="brand-name">TenPeak IT</div>
  <h1 class="offer-title offer-title--first">First<br>Offering:</h1>
  <p class="offer-subtitle">Free Computer System<br>Health Report And Audit</p>
  <ul class="feature-list feature-list--front">
    <li>Health check of servers, workstations and network</li>
    <li>Comprehensive non-technical report including recommendations</li>
  </ul>
</section>

<section class="flyer-side flyer-side--back">
  <svg class="side-art" viewBox="0 0 428 908" preserveAspectRatio="none">
    <defs>
      <linearGradient id="backBlue" x1="0" y1="0" x2="1" y2="1">
        <stop offset="0" stop-color="#12357e"/>
        <stop offset=".6" stop-color="#1a4fb0"/>
        <stop offset="1" stop-color="#1c6fd0"/>
      </linearGradient>
      <linearGradient id="teamPhoto" x1="0" y1="0" x2="1" y2="1">
        <stop offset="0" stop-color="#eef1f5"/>
        <stop offset=".5" stop-color="#e3dcd3"/>
        <stop offset="1" stop-color="#cdbba6"/>
      </linearGradient>
      <linearGradient id="ring" x1="0" y1="0" x2="0" y2="1">
        <stop offset="0" stop-color="#f6a21e"/>
        <stop offset="1" stop-color="#c8321a"/>
      </linearGradient>
      <radialGradient id="coin" cx=".45" cy=".4" r=".7">
        <stop offset="0" stop-color="#fff4b8"/>
        <stop offset="1" stop-color="#eeb21c"/>
      </radialGradient>
      <path id="badgeArc" d="M207 534 A72 72 0 1 1 309 534"/>
    </defs>
    <rect width="428" height="908" fill="url(#backBlue)"/>
    <path d="M0 22 Q200 -2 428 8 L428 388 Q250 382 0 340 Z" fill="url(#teamPhoto)" role="img" aria-label="Photo of a smiling four-person office team"/>
    <polygon fill="#3866b8" stroke="#1f4690" stroke-width="2" points="360,300 324,319 340,346 293,351 285,380 241,370 210,392 179,370 135,380 127,351 80,346 96,319 60,300 96,281 80,254 127,249 135,220 179,230 210,208 241,230 285,220 293,249 340,254 324,281"/>
    <rect y="868" width="428" height="40" fill="#1c72d4"/>
    <g class="price-badge">
      <circle cx="258" cy="483" r="90" fill="url(#ring)" stroke="#f7c440" stroke-width="3"/>
      <circle cx="258" cy="483" r="55" fill="url(#coin)" stroke="#d99a18" stroke-width="2"/>
      <text font-family="Belleza, sans-serif" font-size="18" font-weight="700" fill="#ffffff" letter-spacing=".5">
        <textPath href="#badgeArc" startOffset="50%" text-anchor="middle">Discounted technical support</textPath>
      </text>
      <text x="258" y="490" text-anchor="middle" font-family="Belleza, sans-serif" font-size="48" font-weight="700" fill="#1a1a1a">$80</text>
      <text x="258" y="512" text-anchor="middle" font-family="Belleza, sans-serif" font-size="18" fill="#1a1a1a">per hour</text>
      <g fill="#ffffff">
        <polygon points="220,535 222.4,541 228.5,541 223.6,544.8 225.4,551 220,547.2 214.6,551 216.4,544.8 211.5,541 217.6,541"/>
        <polygon points="258,542 260.4,548 266.5,548 261.6,551.8 263.4,558 258,554.2 252.6,558 254.4,551.8 249.5,548 255.6,548"/>
        <polygon points="296,535 298.4,541 304.5,541 299.6,544.8 301.4,551 296,547.2 290.6,551 292.4,544.8 287.5,541 293.6,541"/>
      </g>
    </g>
  </svg>

  <h2 class="offer-title offer-title--second">Second<br>Offering:</h2>
  <ul class="feature-list feature-list--back">
    <li>Day To Day Helpdesk Support</li>
    <li>System Upgrades And Migrations</li>
    <li>Cloud Services Design, Implementation And Support</li>
    <li>Web Hosting, Domain Names And Email Filtering</li>
  </ul>
  <div class="contact-box">
    <div class="contact-row">Phone<span class="colon">:</span></div>
    <div class="contact-row">Email<span class="colon">:</span></div>
    <div class="contact-row">Web Address<span class="colon">:</span></div>
  </div>
</section>

</body>
</html>
```